Header and Full-Page Flyer needed for 2021 Lone Prairie Civic Builders Summit

Save the Date Flyer and Header needed for Q-MarvEt's 2021 Lone Prairie Civic Builders Summit. The Lone Prairie Civic Builders Summit is developed by Owners, for Owners (and other industry stakeholders.

DO NOT INCLUDE This in your design - for reference on design ideas only.
About the The Lone Prairie Civic Builders Summit:

Are you working within the boundaries of a smaller town mentality?
Do you feel stuck within your Big City limits?

The Lone Prairie Civic Builders Summit is where municipalities, counties, ISD's, and other public entities will come together to share what they know, and define what they want to know more about capital project planning design, delivery, and operations.

Font styles to use
Sans Serif

Requirements
Must have
• Lone Prairie Civic Builders Summit
Date: August 5, 2021
Location: San Antonio, TX

```html
<!DOCTYPE html>
<html lang="en">
<head>
<meta charset="utf-8">
<title>Lone Prairie Civic Builders Summit – Save the Date</title>
<link href="https://fonts.googleapis.com/css2?family=Montserrat:ital,wght@0,400;0,500;0,700;0,800;1,500&family=Nunito:wght@800;900&display=swap" rel="stylesheet">
<style>
  :root {
    --stage: #2b2b2b;
    --paper: #ffffff;
    --brand-blue: #1d4192;
    --brand-green: #8db442;
    --slate: #4d4d4f;
    --warm: #f2a488;
    --rose: #e0555a;
    --teal: #7fbcb2;
  }
  * { margin: 0; padding: 0; box-sizing: border-box; }
  html, body { width: 1200px; height: 1200px; overflow: hidden; background: var(--stage); }
  .flyer {
    position: absolute; left: 231px; top: 126px;
    width: 738px; height: 956px;
    background: var(--paper); overflow: hidden;
    font-family: "Montserrat", sans-serif;
  }
  .city-photo {
    position: absolute; left: 0; top: 150px; width: 738px; height: 600px;
    background: linear-gradient(90deg, var(--rose) 0%, var(--warm) 30%, #d9c1b6 55%, #9bc9c0 78%, var(--teal) 100%);
  }
  .city-photo::after {
    content: ""; position: absolute; inset: 0;
    background: linear-gradient(180deg, #fff 0%, rgba(255,255,255,0.75) 30%, rgba(255,255,255,0.1) 65%, rgba(255,255,255,0) 100%);
  }
  .state-map {
    position: absolute; left: 113px; top: 118px; width: 250px; height: 250px;
    background: radial-gradient(circle, rgba(29,65,146,0.08) 0%, rgba(29,65,146,0) 70%);
  }
  .shapes { position: absolute; left: 0; top: 0; }
  .brand { position: absolute; left: 278px; top: 42px; display: flex; align-items: center; gap: 12px; }
  .brand-dot { width: 52px; height: 52px; border-radius: 50%; background: var(--brand-blue); }
  .brand-name { font-weight: 500; font-size: 30px; color: var(--slate); letter-spacing: -0.5px; }
  .presents { position: absolute; left: 349px; top: 110px; font-style: italic; font-weight: 500; font-size: 20px; color: var(--brand-blue); }
  .event-title { position: absolute; right: 152px; top: 196px; text-align: right; font-family: "Nunito", sans-serif; }
  .event-title .line-main { font-weight: 900; font-size: 50px; color: var(--brand-blue); line-height: 58px; letter-spacing: -0.5px; }
  .event-title .line-mid { font-weight: 800; font-size: 28px; color: var(--slate); letter-spacing: 6px; line-height: 40px; margin-right: -6px; }
  .event-title .line-end { font-weight: 800; font-size: 40px; color: var(--brand-green); letter-spacing: 5px; line-height: 48px; margin-right: -5px; }
  .save-date { position: absolute; left: 60px; top: 608px; color: var(--brand-blue); line-height: 58px; }
  .save-date span { display: block; font-size: 66px; letter-spacing: -1px; }
  .save-date .heavy { font-weight: 800; }
  .save-date .light { font-weight: 400; padding-left: 26px; }
  .prompts { position: absolute; color: #fff; font-size: 17px; line-height: 19.5px; text-align: right; font-weight: 500; }
  .prompt-town { right: 323px; top: 732px; }
  .prompt-city { right: 342px; top: 869px; }
  .details { position: absolute; left: 436px; top: 708px; width: 300px; text-align: center; color: var(--brand-blue); }
  .details .label { font-weight: 400; font-size: 23px; line-height: 28px; }
  .details .value { font-weight: 800; font-size: 31px; line-height: 36px; }
  .details .gap { margin-top: 8px; }
</style>
</head>
<body>
  <main class="flyer">
    <div class="city-photo" role="img" aria-label="City skyline with business people silhouettes, warm red to teal tones"></div>
    <div class="state-map" role="img" aria-label="Outline of the state map behind the title"></div>

    <svg class="shapes" width="738" height="956" viewBox="0 0 738 956" aria-hidden="true">
      <path d="M0,365 C20,440 80,500 160,530 C230,555 300,568 365,573 C260,572 130,545 60,510 C30,495 10,485 0,480 Z" fill="var(--brand-blue)"/>
      <path d="M0,480 C60,540 200,582 328,582 C450,580 530,600 610,660 C665,700 710,730 738,745 L738,956 L0,956 Z" fill="var(--brand-green)"/>
      <path d="M0,912 C120,905 200,860 300,790 C400,720 500,665 620,655 C680,652 720,690 738,738 L738,956 L0,956 Z" fill="var(--brand-blue)"/>
      <path d="M297,719 C420,645 560,610 650,640 C700,660 725,695 738,728" fill="none" stroke="var(--brand-blue)" stroke-width="4"/>
      <circle cx="594" cy="846" r="182" fill="var(--brand-green)"/>
      <circle cx="600" cy="846" r="160" fill="var(--paper)"/>
    </svg>

    <div class="brand">
      <div class="brand-dot"></div>
      <div class="brand-name">Q-MarvEt</div>
    </div>
    <div class="presents">presents</div>

    <h1 class="event-title">
      <div class="line-main">Lone Prairie</div>
      <div class="line-mid">Civic Builders</div>
      <div class="line-end">Summit</div>
    </h1>

    <div class="save-date">
      <span class="heavy">SAVE</span>
      <span class="light">THE</span>
      <span class="heavy">DATE</span>
    </div>

    <p class="prompts prompt-town">Are you<br>working<br>within the<br>boundaries of<br>a smaller town<br>mentality?</p>
    <p class="prompts prompt-city">Do you feel<br>stuck within your Big City limits?</p>

    <div class="details">
      <div class="label">Date:</div>
      <div class="value">August 5,<br>2021</div>
      <div class="label gap">Location:</div>
      <div class="value">San Antonio,<br>TX</div>
    </div>
  </main>
</body>
</html>
```